Plumbing Company- Mass mailing Post card

Name of our company is Bramwell plumbing, Inc. Located in West Palm Beach, Florida. Tag line is "Our service is what set's us apart". We're looking for a postcard that we can send as a mass mailing (QPMX). Our clients are high end so we're looking for classy, simple, clean and easy to read (not busy), to represent the kind of work we do, (our work is like no other). Want an attention getter that manages to get the customer to turn the card over for more info.
Include: phone # 561-555-0193, website www.brwplumbing.example, License CFC9073651
Samples that can be included:
-Tap in to 30 plus years of experience.
-Our reputation is our best asset
-Call Bramwell Plumbing today and let us take care of your plumbing needs.
-Bramwell services offered
-We are the difference!
-Serving the Palm Beaches!

Target Market(s)

High end, owners and Property managers

Industry/Entity Type

Plumbing

Font styles to use
Serif

Requirements
Must have
• Tag line
• Classy and clean
Nice to have
• Our original logo color is blue/grey but not opposed if something different is suggested.
• Interested in seeing ideas
Should not have
• Not to be busy looking.

```html
<!DOCTYPE html>
<html lang="en">
<head>
<meta charset="utf-8">
<title>Bramwell Plumbing – Postcard</title>
<link rel="stylesheet" href="https://fonts.googleapis.com/css2?family=Tinos:ital,wght@0,400;0,700;1,400;1,700&family=Open+Sans:wght@700&family=Arimo:wght@400;700&display=swap">
<style>
  :root {
    --bg: #d9d7d4;
    --card: #ffffff;
    --charcoal: #3a3a3c;
    --brand-blue: #27418f;
    --text-grey: #5a5a5a;
    --white: #ffffff;
    --tick: #c9c9c9;
  }
  * { box-sizing: border-box; margin: 0; padding: 0; }
  html, body { width: 1009px; height: 1200px; overflow: hidden; background: var(--bg); }
  body { position: relative; font-family: "Tinos", serif; }

  .card { position: absolute; width: 741px; background: var(--card); overflow: hidden; box-shadow: 0 2px 6px rgba(0,0,0,.18); }
  .card--front { left: 121px; top: 64px; height: 504px; }
  .card--back { left: 187px; top: 615px; height: 503px; }

  .photo { position: absolute; }
  .photo--hero { left: 0; top: 0; width: 351px; height: 316px;
    background: linear-gradient(180deg, #3c3c3e 0%, #55534f 30%, #8a8378 48%, #e6e2dc 62%, #d8d3cb 70%, #2b2b2d 76%, #1d1d1f 100%); }
  .photo--bath-suite { left: 362px; top: 0; width: 186px; height: 154px;
    background: linear-gradient(180deg, #d9c49c 0%, #f2e8d4 35%, #e6d2ae 65%, #b99566 100%); }
  .photo--gold-faucet { left: 560px; top: 0; width: 181px; height: 154px;
    background: linear-gradient(180deg, #f3e6d2 0%, #ead6b8 40%, #b98c55 52%, #efdcc2 62%, #e3c9a6 100%); }
  .photo--pot-filler { left: 362px; top: 162px; width: 186px; height: 154px;
    background: linear-gradient(180deg, #f3efe8 0%, #e9e2d7 60%, #c8b59a 82%, #8c6a45 100%); }
  .photo--spa-bath { left: 560px; top: 162px; width: 181px; height: 154px;
    background: linear-gradient(180deg, #6b4a2a 0%, #c9ad7f 25%, #e7d6b2 60%, #6e7d4a 85%, #f2eee6 100%); }
  .photo--farm-sink { left: 0; top: 325px; width: 351px; height: 100px;
    background: linear-gradient(180deg, #1f2a1c 0%, #4a5a38 40%, #7c8a66 62%, #e7e9ea 80%, #f4f5f6 100%); }
  .photo--vanity { left: 360px; top: 325px; width: 381px; height: 100px;
    background: linear-gradient(180deg, #ece2d4 0%, #e2d3bf 45%, #2b2624 62%, #7a4f33 80%, #5e3b25 100%); }

  .sink-caption { position: absolute; left: 22px; top: 340px; color: var(--white); font-size: 9.5px; line-height: 12px; }
  .sink-caption .indent { padding-left: 36px; font-style: italic; }
  .sink-button { position: absolute; left: 82px; top: 371px; width: 67px; height: 14px; border: 1px solid rgba(255,255,255,.8); color: var(--white); font-style: italic; font-size: 6.5px; line-height: 12px; text-align: center; }

  .front-tagline { position: absolute; left: 16px; top: 18px; color: var(--white); font-style: italic; font-size: 19px; line-height: 21px; }

  .front-footer { position: absolute; left: 0; top: 436px; width: 741px; height: 68px; background: var(--charcoal); }
  .front-footer .brand { position: absolute; left: 24px; top: 20px; display: flex; align-items: center; gap: 8px; color: var(--white); font-weight: 700; font-size: 22px; }
  .brand-dot { width: 14px; height: 14px; border-radius: 50%; background: #5b79c4; }
  .front-footer .cta { position: absolute; right: 18px; top: 9px; color: var(--white); font-style: italic; font-weight: 700; font-size: 12.5px; }
  .front-footer .phone { position: absolute; right: 18px; top: 28px; display: flex; align-items: center; gap: 8px; color: var(--white); font-family: "Open Sans", sans-serif; font-weight: 700; font-size: 19px; }

  .back-brand { position: absolute; left: 44px; top: 34px; display: flex; align-items: center; gap: 10px; color: var(--brand-blue); font-weight: 700; font-size: 25px; }
  .back-brand .brand-dot { width: 22px; height: 22px; background: var(--brand-blue); }
  .license { position: absolute; left: 301px; top: 71px; font-family: "Arimo", sans-serif; font-style: italic; font-size: 9px; color: var(--text-grey); }

  .return-address { position: absolute; left: 460px; top: 42px; font-size: 14.5px; line-height: 18px; color: var(--text-grey); font-style: normal; }
  .return-address .name { color: var(--brand-blue); }
  .return-address .line { padding-left: 4px; }

  .indicia { position: absolute; left: 640px; top: 21px; width: 80px; height: 80px; border: 1px solid #555; font-family: "Arimo", sans-serif; font-size: 10.5px; line-height: 13px; text-align: center; padding-top: 7px; color: #111; }
  .indicia b { font-weight: 700; }

  .mail-panel { position: absolute; left: 0; top: 109px; width: 419px; height: 224px; background: var(--charcoal); color: var(--white); }
  .mail-panel h1 { font-style: italic; font-weight: 400; font-size: 28px; text-align: center; margin-top: 21px; }
  .benefits { list-style: none; margin: 20px 0 0 26px; }
  .benefits li { display: flex; align-items: center; gap: 9px; font-size: 18px; line-height: 26px; }
  .benefits svg { flex: none; }

  .photo--tub-faucet { left: 0; top: 338px; width: 419px; height: 116px; background: linear-gradient(120deg, #1e1e20 0%, #3a3a3c 35%, #b9d7cc 60%, #e6f1ed 100%); }

  .web-band { position: absolute; left: 0; top: 461px; width: 419px; height: 42px; background: var(--charcoal); color: var(--white); text-align: center; font-size: 25px; line-height: 42px; }

  .addressee { position: absolute; left: 467px; top: 205px; width: 253px; height: 75px; border: 1px solid #333; padding: 20px 0 0 26px; font-family: "Arimo", sans-serif; font-size: 13.5px; line-height: 16px; color: #111; }
</style>
</head>
<body>

<section class="card card--front" aria-label="Postcard front">
  <div class="photo photo--hero" role="img" aria-label="Luxury kitchen sink with gold bridge faucet on marble counter at night"></div>
  <p class="front-tagline">Our service is what<br>set's us apart</p>
  <div class="photo photo--bath-suite" role="img" aria-label="Grand cream and gold master bathroom with soaking tub"></div>
  <div class="photo photo--gold-faucet" role="img" aria-label="Rose gold bridge faucet against diamond tile backsplash"></div>
  <div class="photo photo--pot-filler" role="img" aria-label="Wall-mounted pot filler faucet over stove with vegetables"></div>
  <div class="photo photo--spa-bath" role="img" aria-label="Spa bathroom with arched doorways and freestanding tub"></div>
  <div class="photo photo--farm-sink" role="img" aria-label="Fireclay farmhouse sink with bridge faucet by garden window"></div>
  <p class="sink-caption">Halden · Originator of<br><span class="indent">the True Fireclay Sink</span></p>
  <p class="sink-button">Discover Halden</p>
  <div class="photo photo--vanity" role="img" aria-label="Modern vanity with rectangular vessel sinks and towel warmer"></div>

  <footer class="front-footer">
    <div class="brand"><span class="brand-dot"></span>Bramwell Plumbing</div>
    <p class="cta">Call Bramwell Plumbing today and let us take care of your plumbing needs.</p>
    <p class="phone">
      <svg width="20" height="20" viewBox="0 0 20 20" aria-hidden="true"><circle cx="10" cy="10" r="9" fill="none" stroke="#fff" stroke-width="1.6"/><path d="M7 5.5l1.6 2.2-1 1.2c.6 1.4 1.6 2.4 3 3l1.2-1 2.2 1.6-.8 1.6c-3.6-.2-6.6-3.2-6.8-6.8z" fill="#fff"/></svg>
      561-555-0193
    </p>
  </footer>
</section>

<section class="card card--back" aria-label="Postcard back">
  <div class="back-brand"><span class="brand-dot"></span>Bramwell Plumbing</div>
  <p class="license">License CFC9073651</p>

  <address class="return-address">
    <div class="name">Bramwell Plumbing</div>
    <div class="line">West Palm Beach, FL</div>
    <div class="line">561-555-0193</div>
  </address>

  <div class="indicia">PRSRT STD<br>ECRWSS<br>U.S.POSTAGE<br><b>PAID</b><br>QPMX RETAIL</div>

  <div class="mail-panel">
    <h1>Our service is what set's us apart</h1>
    <ul class="benefits">
      <li><svg width="14" height="14" viewBox="0 0 14 14" aria-hidden="true"><circle cx="7" cy="7" r="7" fill="var(--tick)"/><path d="M4 7.2l2 2 4-4.2" stroke="#3a3a3c" stroke-width="1.6" fill="none"/></svg>30 plus years of experience</li>
      <li><svg width="14" height="14" viewBox="0 0 14 14" aria-hidden="true"><circle cx="7" cy="7" r="7" fill="var(--tick)"/><path d="M4 7.2l2 2 4-4.2" stroke="#3a3a3c" stroke-width="1.6" fill="none"/></svg>Our reputation is our best asset</li>
      <li><svg width="14" height="14" viewBox="0 0 14 14" aria-hidden="true"><circle cx="7" cy="7" r="7" fill="var(--tick)"/><path d="M4 7.2l2 2 4-4.2" stroke="#3a3a3c" stroke-width="1.6" fill="none"/></svg>Bramwell services offered</li>
      <li><svg width="14" height="14" viewBox="0 0 14 14" aria-hidden="true"><circle cx="7" cy="7" r="7" fill="var(--tick)"/><path d="M4 7.2l2 2 4-4.2" stroke="#3a3a3c" stroke-width="1.6" fill="none"/></svg>We are the difference!</li>
      <li><svg width="14" height="14" viewBox="0 0 14 14" aria-hidden="true"><circle cx="7" cy="7" r="7" fill="var(--tick)"/><path d="M4 7.2l2 2 4-4.2" stroke="#3a3a3c" stroke-width="1.6" fill="none"/></svg>Serving the Palm Beaches!</li>
    </ul>
  </div>

  <div class="photo photo--tub-faucet" role="img" aria-label="Chrome tub faucet on black granite over foaming bath water"></div>

  <div class="web-band">www.brwplumbing.example</div>

  <div class="addressee">Local<br>Postal Customer</div>
</section>

</body>
</html>
```